Orbell Consulting- executive coaching business

looking for business card design for a newly started coaching business.
specialising in Exective coaching, Leadership, NLP and Motivation.
Looking for a simple, classy design using the existing logo attached and colour themes that complement the logo.
No red or orange in the business card design please.

Target Market(s)

Defence and Veteran community

Industry/Entity Type

Life Coaching

Contact Information for Business Card

looking for business cards for newly started coaching business.
specialising in Exective Coaching, Leadership, NLP and Motivation

Font styles to use
Serif
Script

Colors
0556a4
3176b5
86cfc6
33b8a4

Requirements
Must have
• Logo
• Email address- Jess@orbellconsulting.com.au
• Contact number
• Services provided - Executive Coaching, Leadership, NLP and Motivational Mapping.
Nice to have
• Same colours as logo
Should not have
• Red or orange

```html
<!DOCTYPE html>
<html lang="en">
<head>
<meta charset="utf-8">
<title>Orbell Consulting – Business Card</title>
<link href="https://fonts.googleapis.com/css2?family=Lato:wght@400;700&display=swap" rel="stylesheet">
<style>
  :root {
    --blue: #3176b5;
    --blue-deep: #0556a4;
    --green: #3cc46e;
    --grey: #7a7a7a;
    --ink: #1d1d1d;
    --paper: #ffffff;
    --backdrop: #dfe3e6;
  }
  * { margin: 0; padding: 0; box-sizing: border-box; }
  html, body { width: 1200px; height: 960px; overflow: hidden; }
  body {
    background: var(--backdrop);
    font-family: "Lato", Arial, sans-serif;
    display: flex;
    flex-direction: column;
    align-items: center;
    justify-content: center;
    gap: 50px;
  }
  .card {
    position: relative;
    width: 700px;
    height: 400px;
    overflow: hidden;
    box-shadow: 0 6px 18px rgba(0,0,0,.18);
  }
  .card-front { background: var(--paper); }
  .card-back { background: var(--blue); color: #fff; }
  .swoosh { position: absolute; inset: 0; width: 100%; height: 100%; }

  .brand {
    position: absolute;
    display: flex;
    flex-direction: column;
    align-items: center;
  }
  .brand-mark {
    width: 76px; height: 76px;
    border-radius: 50%;
    border: 3px solid currentColor;
  }
  .brand-name {
    margin-top: 12px;
    font-weight: 700;
    font-size: 30px;
    letter-spacing: .5px;
    text-transform: uppercase;
    white-space: nowrap;
  }
  .card-front .brand { top: 34px; right: 50px; color: var(--blue-deep); }
  .card-front .brand-mark { border-color: var(--grey); }

  .holder-name {
    position: absolute;
    top: 196px; right: 56px;
    font-size: 24px;
    color: var(--blue-deep);
  }
  .contact-list {
    position: absolute;
    left: 60px; top: 236px;
    list-style: none;
    font-size: 19px;
    color: var(--ink);
  }
  .contact-list li { display: flex; align-items: center; gap: 14px; height: 26px; }
  .contact-list svg { width: 16px; height: 16px; fill: var(--blue); flex: none; }

  .card-back .brand { left: 0; right: 0; top: 80px; color: #fff; }
  .card-back .brand-name { font-size: 36px; }
  .rule {
    width: 340px; height: 3px; margin-top: 10px;
    background: var(--green);
  }
  .services {
    position: absolute;
    left: 0; right: 0; bottom: 72px;
    text-align: center;
    font-size: 17px;
    letter-spacing: .4px;
  }
  .services .dot { margin: 0 6px; }
</style>
</head>
<body>

<section class="card card-front">
  <svg class="swoosh" viewBox="0 0 700 400" aria-hidden="true">
    <path d="M0 0 H320 C180 20 40 90 0 250 Z" fill="var(--blue)"/>
    <path d="M300 30 C170 55 70 110 30 225 C60 140 150 75 300 30 Z" fill="var(--green)"/>
    <path d="M0 345 C220 395 560 395 700 235 V400 H0 Z" fill="var(--blue)"/>
    <path d="M420 328 C540 315 640 275 690 205 C630 285 540 320 420 332 Z" fill="var(--green)"/>
  </svg>

  <div class="brand">
    <span class="brand-mark"></span>
    <span class="brand-name">Orbell Consulting</span>
  </div>

  <p class="holder-name">Jess Marlowe</p>

  <ul class="contact-list">
    <li>
      <svg viewBox="0 0 16 16"><path d="M3 1l3 3-1.5 2a9 9 0 005.5 5.5L12 10l3 3-2 2C7 15 1 9 1 3z"/></svg>
      512 004 2290
    </li>
    <li>
      <svg viewBox="0 0 16 16"><path d="M4 0h8v16H4zM5.5 2v10h5V2z"/></svg>
      512 004 2291
    </li>
    <li>
      <svg viewBox="0 0 16 16"><path d="M0 3h16v10H0z"/><path d="M1.5 4.5L8 9l6.5-4.5" fill="none" stroke="#fff" stroke-width="1.2"/></svg>
      Jess@orbellconsulting.com.au
    </li>
  </ul>
</section>

<section class="card card-back">
  <div class="brand">
    <span class="brand-mark"></span>
    <span class="brand-name">Orbell Consulting</span>
    <span class="rule"></span>
  </div>
  <p class="services">
    Executive Coaching<span class="dot">•</span>Leadership<span class="dot">•</span>NLP<span class="dot">•</span>Motivational Mapping
  </p>
</section>

</body>
</html>
```